Creative Landscape Architecture Company Needs a Creative Business Card Design

Marsh and Partners, Inc. is a landscape architecture (LA) company started in 1997 in Austin, TX. We work on large commerical projects all around the U.S. and provide land planning, site planning, landscape design and architectural renderings.

We don't want this card to look like a LA firm's business card. We are looking for a business card design that is edgy and cool to reflect the more artistic and creative side of our company. We would like our clients to think "now there's a business card unlike any other LA that I've seen before."

We would like it to be in standard 2"x3.5" format. Double sided. Full color ok. Our company logo is attached. We like the logo but would not be adverse to any variations you would like to make to it. Feel free to change it up. Typically the logo has been a light saturated orange color but its not necessary that you stick with it.

Requirements
Must have
• 1. Company name
2. individuals name
3. email address
4. cell number
5. office number
6. website: www.marshandpartners-demo.net
7. Business address
Nice to have
• Can add (but not necessary)
Personal titles such as "president" or "registered landscape architect"

```html
<!DOCTYPE html>
<html lang="en">
<head>
<meta charset="utf-8">
<title>Marsh and Partners – Business Card</title>
<link rel="stylesheet" href="https://fonts.googleapis.com/css2?family=Didact+Gothic&display=swap">
<style>
  :root {
    --steel-blue: #5b83a1;
    --band-blue: #7d9ab1;
    --pale-blue: #c9d6e0;
    --paper: #f3f3f1;
    --ink: #2b2b2b;
    --backdrop: #e6e6e4;
  }
  * { box-sizing: border-box; margin: 0; padding: 0; }
  html, body {
    width: 1200px; height: 900px; overflow: hidden;
    background: var(--backdrop);
    font-family: "Didact Gothic", "Century Gothic", sans-serif;
  }
  .stage {
    position: relative; width: 1200px; height: 900px;
    display: flex; justify-content: center; align-items: center; gap: 90px;
  }
  .card {
    position: relative; width: 360px; height: 630px;
    background: var(--paper);
    box-shadow: 0 6px 18px rgba(0,0,0,0.18);
    overflow: hidden;
  }
  /* Front */
  .card-front .ornament {
    position: absolute; left: 0; top: 0; width: 100%; height: 530px;
    background: linear-gradient(160deg, var(--steel-blue) 0%, var(--pale-blue) 45%, var(--paper) 70%, var(--steel-blue) 100%);
  }
  .card-front .name-band {
    position: absolute; left: 0; top: 530px; width: 100%; height: 64px;
    background: var(--band-blue);
    display: flex; align-items: center; padding-left: 26px;
  }
  .card-front .company-name {
    color: var(--paper); font-size: 31px; letter-spacing: 0.5px;
  }
  .card-front .base-strip {
    position: absolute; left: 0; top: 594px; width: 100%; height: 36px;
    background: var(--steel-blue);
  }
  /* Back */
  .card-back .title-band {
    position: absolute; left: 0; top: 26px; width: 100%; height: 82px;
    background: var(--band-blue);
    padding: 10px 22px; color: var(--paper);
  }
  .card-back .person-name { font-size: 28px; line-height: 1.1; }
  .card-back .person-role { font-size: 19px; line-height: 1.2; }
  .card-back .contact {
    position: absolute; left: 22px; top: 128px; right: 14px;
    font-size: 15px; line-height: 1.45; color: var(--ink);
  }
  .card-back .contact .label { color: var(--steel-blue); }
  .card-back .address { margin-top: 6px; }
  .card-back .website {
    margin-top: 6px; color: var(--steel-blue); font-weight: bold; font-size: 16px;
  }
  .card-back .ornament {
    position: absolute; left: 0; top: 340px; width: 100%; height: 290px;
    background: linear-gradient(175deg, var(--paper) 0%, var(--pale-blue) 40%, var(--steel-blue) 100%);
  }
</style>
</head>
<body>
  <main class="stage">
    <section class="card card-front" aria-label="Card front">
      <div class="ornament" role="img" aria-label="Large decorative acanthus leaf scroll in steel blue and white"></div>
      <div class="name-band"><span class="company-name">Marsh and Partners</span></div>
      <div class="base-strip"></div>
    </section>

    <section class="card card-back" aria-label="Card back">
      <header class="title-band">
        <div class="person-name">Daniel Marsh</div>
        <div class="person-role">President</div>
      </header>
      <div class="contact">
        <div><span class="label">M:</span> +1 (512) 555 0142</div>
        <div><span class="label">T :</span> +1 (512) 555 0142</div>
        <div><span class="label">E :</span> daniel@marshandpartners-demo.net</div>
        <div class="address">Juniper Hollow Road 8,<br>78704 TX Austin,<br>The Country</div>
        <div class="website">www.marshandpartners-demo.net</div>
      </div>
      <div class="ornament" role="img" aria-label="Decorative acanthus leaf scroll in steel blue rising from the card's lower edge"></div>
    </section>
  </main>
</body>
</html>
```